KFL Noblesville Sign

I need to have a sign designed for a new self-storage facility we are going to be opening. The sign will be 4'W X 8'H.

Industry/Entity Type

Self Storage

Requirements
Must have
• Keystone Locker Hub logo at the top of the sign, under the logo I want the rendering.
• I also must have this information on the sign:
• 1. OPENING FALL 2016
• 2. Your premier self-storage facility.
• 3. www.keystonelockerhub.com

```html
<!DOCTYPE html>
<html lang="en">
<head>
<meta charset="utf-8">
<title>Keystone Locker Hub – Opening Sign</title>
<link rel="stylesheet" href="https://fonts.googleapis.com/css2?family=Oswald:wght@700&family=Source+Sans+3:wght@400;600&display=swap">
<style>
  :root {
    --backdrop: #ecebe7;
    --sign-white: #ffffff;
    --sign-yellow: #ffed29;
    --sign-green: #139e48;
    --sign-red: #ec1c24;
    --url-ink: #fff9c4;
  }
  html, body {
    margin: 0;
    padding: 0;
    width: 1200px;
    height: 1200px;
    overflow: hidden;
    background: var(--backdrop);
  }
  .canvas {
    position: relative;
    width: 1200px;
    height: 1200px;
  }
  .sign {
    position: absolute;
    left: 320px;
    top: 40px;
    width: 560px;
    height: 1120px;
    display: block;
  }
  .sign__card { fill: var(--sign-white); }
  .sign__frame { fill: var(--sign-green); }
  .sign__panel { fill: var(--sign-yellow); }
  .sign__band { fill: var(--sign-green); }
  .brand-name {
    font-family: "Oswald", "Arial Narrow", sans-serif;
    font-weight: 700;
    fill: var(--sign-red);
  }
  .headline {
    font-family: "Oswald", "Arial Narrow", sans-serif;
    font-weight: 700;
    fill: var(--sign-red);
  }
  .headline__year { fill: var(--sign-green); }
  .tagline {
    font-family: "Source Sans 3", "Myriad Pro", sans-serif;
    fill: var(--sign-red);
  }
  .tagline--light { font-weight: 400; }
  .tagline--strong { font-weight: 600; }
  .web-address {
    font-family: "Source Sans 3", "Myriad Pro", sans-serif;
    font-weight: 400;
    fill: var(--url-ink);
  }
</style>
</head>
<body>
<main class="canvas">
  <svg class="sign" viewBox="0 0 549 1098" xmlns="http://www.w3.org/2000/svg" role="img" aria-label="Keystone Locker Hub opening sign">
    <rect class="sign__card" x="0" y="0" width="549" height="1098"/>
    <polygon class="sign__frame" points="14,17 537,17 497,1085 52,1085"/>
    <polygon class="sign__panel" points="25,28 526,28 487,1074 62,1074"/>
    <polygon class="sign__band" points="59,1003 490,1003 489,1043 60,1043"/>

    <g class="brand" text-anchor="middle">
      <text class="brand-name" x="274" y="152" font-size="66">Keystone</text>
      <text class="brand-name" x="274" y="238" font-size="66">Locker</text>
      <text class="brand-name" x="274" y="324" font-size="66">Hub</text>
    </g>

    <g class="headline-group" text-anchor="middle">
      <text class="headline" x="274" y="523" font-size="98" textLength="345" lengthAdjust="spacingAndGlyphs">OPENING</text>
      <text class="headline" x="274" y="608" font-size="98" textLength="345" lengthAdjust="spacingAndGlyphs">FALL <tspan class="headline__year">2016</tspan></text>
    </g>

    <g class="tagline-group" text-anchor="middle">
      <text class="tagline tagline--light" x="274" y="729" font-size="34">Your</text>
      <text class="tagline tagline--strong" x="274" y="779" font-size="44">Premier</text>
      <text class="tagline tagline--light" x="274" y="847" font-size="58" textLength="400" lengthAdjust="spacingAndGlyphs">SELF-STORAGE</text>
      <text class="tagline tagline--light" x="274" y="914" font-size="58">FACILITY</text>
    </g>

    <text class="web-address" x="274" y="1031" font-size="24" text-anchor="middle">www.keystonelockerhub.com</text>
  </svg>
</main>
</body>
</html>
```